Original catchy book cover

I need a book cover for my book "The Steady Harbor Manual" (https://quillpress.example/harbormanual). This will be a book self published on brightmart.
The book talks about the following concepts:
- Iterative product delivery
- Early discovery using feedback from customers
- Start small, think big, move fast
- Slice the product into valuable increments that can be validated with customers
- Experimental approach to deciding the next slice of work
A simple cover that stands out from the business books already out there! Some examples are:
https://www.brightmart.example/Field-Notes-Thriving-Teams-Steadily-ebook/dp/Q00XTR4KWZ/ref=sr_1_1?ie=UTF8&qid=1500000001&sr=8-1&keywords=field+notes
https://www.brightmart.example/Quiet-Harbor-Almanac-Shape-Offerings-ebook/dp/Q00MVK219J/ref=sr_1_1?s=digital-text&ie=UTF8&qid=1500000002&sr=1-1&keywords=quiet+harbor+almanac
https://www.brightmart.example/Course-Charts-Renewed-Heading-Fog-ebook/dp/Q099WT71ZD/ref=pd_sim_351_2?_encoding=UTF8&psc=1&refRID=9QZTRWJDDAV52LM0NKPP
Lastly, attached are 2 draft covers that i've been playing with. Would love a graphic as part of the cover if it makes sense in your design! The graphic should tie to the meaning or themes of the book. Emphasis on ways of working, collaboration, experimentation, hypothesis, agile, incremental or adaptive. Those are some words that describe the content of the book.
Alternatively, something abstract could also be an option if a literal graphic doesn't suit the theme of your design.
Target Market(s)
Product owners, scrum masters, people in the agile community, software developers, designers
Industry/Entity Type
Information Technology
Font styles to use
Colors
Designer to choose colors to be used in the design.
Requirements
Must have
- Title, Subtitle, Author Name
- Back of the book should have space for a description (use lorem ipsum for now)
- Please use the editorial logo
- (please omit "created by Tomas Verlindt" because the editorial logo replaces that.
- The design must be original art or graphics (i.e. it should be similar to another cover in this topic).
Nice to have
- A graphic would be ideal if it is relevant to the book topic, otherwise a nice simple cover that uses colors or patterns that are easy to recall.
- The color suggestions below are suggestions only. Do not feel you have to incorporate all the colors and feel free to recommend an alternate palette.
Should not have
- Clipart or generic stock art photos. Images for the sake of images, traditional logos (e.g. a computer, a phone etc unless it's part of an overall theme that ties the logos together).

```html
<!DOCTYPE html>
<html lang="en">
<head>
<meta charset="utf-8">
<title>The Steady Harbor Manual — Full Cover</title>
<link rel="stylesheet" href="https://fonts.googleapis.com/css2?family=Bebas+Neue&family=Oswald:wght@200;300&family=EB+Garamond&family=Montserrat:wght@400&display=swap">
<style>
  :root {
    --magenta-deep: #cc22b4;
    --magenta-mid: #d54cc2;
    --magenta-soft: #e08fd4;
    --magenta-ink: #c0179f;
    --pattern-dark: rgba(150, 10, 120, 0.35);
    --pattern-light: rgba(255, 220, 250, 0.15);
    --paper: #ffffff;
    --logo-grey: #ece4ea;
  }
  * { margin: 0; padding: 0; box-sizing: border-box; }
  html, body { width: 1200px; height: 830px; overflow: hidden; }
  body { background: #fff; }

  .cover {
    position: relative;
    width: 1200px;
    height: 830px;
    overflow: hidden;
    background: linear-gradient(175deg, var(--magenta-deep) 0%, var(--magenta-mid) 45%, var(--magenta-soft) 100%);
    color: var(--paper);
  }

  .pattern {
    position: absolute;
    transform: rotate(-35deg);
    background: linear-gradient(160deg, var(--pattern-dark), var(--pattern-light));
    border-radius: 4px;
  }
  .pattern--back { left: -120px; top: 520px; width: 640px; height: 360px; }
  .pattern--front { left: 700px; top: 80px; width: 560px; height: 330px; opacity: .8; }

  /* Back cover */
  .back-blurb {
    position: absolute;
    left: 62px; top: 60px;
    width: 436px;
    font-family: "EB Garamond", serif;
    font-size: 17.4px;
    line-height: 20px;
    text-align: justify;
    hyphens: auto;
  }
  .back-blurb p + p { margin-top: 20px; }

  .isbn-space {
    position: absolute;
    left: 61px; top: 696px;
    width: 133px; height: 86px;
    background: var(--paper);
  }

  .imprint {
    position: absolute;
    display: flex;
    align-items: center;
    gap: 12px;
    font-family: "Montserrat", sans-serif;
    font-weight: 400;
    color: var(--logo-grey);
    white-space: nowrap;
  }
  .imprint__dot {
    width: 52px; height: 52px;
    border-radius: 50%;
    border: 7px solid var(--logo-grey);
    flex: none;
  }
  .imprint__name { font-size: 18px; line-height: 20px; }
  .imprint__url { font-size: 13px; line-height: 16px; }
  .imprint--back { left: 228px; top: 706px; }
  .imprint--front { left: 836px; top: 722px; }

  /* Spine */
  .spine-title,
  .spine-author {
    position: absolute;
    writing-mode: vertical-rl;
    white-space: nowrap;
  }
  .spine-title { left: 572px; top: 54px; font-size: 40px; line-height: 40px; }
  .spine-title .bold { font-family: "Bebas Neue", sans-serif; }
  .spine-title .thin { font-family: "Oswald", sans-serif; font-weight: 200; font-size: 37px; }
  .spine-author {
    left: 582px; top: 592px;
    font-family: "Oswald", sans-serif; font-weight: 200;
    font-size: 22px; line-height: 26px; letter-spacing: 4px;
  }

  /* Front cover */
  .front-title {
    position: absolute;
    left: 650px; top: 30px;
    width: 550px;
    text-align: center;
    line-height: 1;
  }
  .front-title span { display: block; white-space: nowrap; }
  .front-title__top {
    font-family: "Bebas Neue", sans-serif;
    font-size: 138px;
    line-height: 130px;
  }
  .front-title__mid {
    font-family: "Oswald", sans-serif;
    font-weight: 200;
    font-size: 128px;
    line-height: 150px;
    letter-spacing: 4px;
  }
  .front-title__bottom {
    font-family: "Bebas Neue", sans-serif;
    font-size: 156px;
    line-height: 150px;
    letter-spacing: 14px;
  }

  .subtitle-band {
    position: absolute;
    left: 646px; top: 475px;
    width: 554px; height: 107px;
    background: var(--paper);
    display: flex;
    align-items: center;
    justify-content: center;
    text-align: center;
    font-family: "Bebas Neue", sans-serif;
    font-size: 33px;
    line-height: 37px;
    letter-spacing: 2px;
    color: var(--magenta-ink);
  }

  .front-author {
    position: absolute;
    left: 650px; top: 614px;
    width: 550px;
    text-align: center;
    white-space: nowrap;
    font-family: "Oswald", sans-serif;
    font-weight: 200;
    font-size: 56px;
    line-height: 64px;
    letter-spacing: 10px;
  }
</style>
</head>
<body>
<main class="cover">
  <div class="pattern pattern--back" role="img" aria-label="Abstract pattern of tilted magenta squares"></div>
  <div class="pattern pattern--front" role="img" aria-label="Abstract pattern of tilted magenta squares"></div>

  <section class="back">
    <div class="back-blurb">
      <p>Lorem ipsum dolor sit amet, consectetur adipiscing elit. Duis non cursus lorem. Nunc id ante elit. In malesuada orci aliquam tincidunt bibendum. Quisque neque eros, fermentum ac pretium id, interdum luctus dui. Ut nisi urna, rutrum eu nisi ultrices, tristique dapibus enim. Nunc tempus mi efficitur nulla placerat, id bibendum lacus feugiat. Maecenas faucibus suscipit luctus. Mauris sit amet justo congue elit pellentesque pharetra lacinia eget felis. Vivamus sed mollis sapien.</p>
      <p>Integer euismod ex justo, sollicitudin porttitor odio posuere ac. Aliquam hendrerit accumsan quam, nec interdum ante fringilla in. Aliquam lobortis metus sit amet ornare tempus. Sed tincidunt tellus quis tempor consequat. Aenean eget magna neque. Nam id sollicitudin orci. Donec ut leo ac nibh consectetur vehicula a quis nunc. Donec nec neque quis erat finibus scelerisque. Nullam egestas tempor libero eu consectetur. Ut quis turpis nec mi maximus ultrices at at eros. Maecenas sit amet efficitur tortor.</p>
    </div>
    <div class="isbn-space"></div>
    <div class="imprint imprint--back">
      <span class="imprint__dot"></span>
      <div>
        <div class="imprint__name">Editora<br>Verlindt</div>
        <div class="imprint__url">verlindt.example</div>
      </div>
    </div>
  </section>

  <section class="spine">
    <div class="spine-title"><span class="bold">THE STEADY </span><span class="thin">HARBOR </span><span class="bold">MANUAL</span></div>
    <div class="spine-author">MIRA CASTELL</div>
  </section>

  <section class="front">
    <h1 class="front-title">
      <span class="front-title__top">THE STEADY</span>
      <span class="front-title__mid">HARBOR</span>
      <span class="front-title__bottom">MANUAL</span>
    </h1>
    <div class="subtitle-band">A practitioner´s guide to building<br>viable products customers love</div>
    <div class="front-author">MIRA CASTELL</div>
    <div class="imprint imprint--front">
      <span class="imprint__dot"></span>
      <div>
        <div class="imprint__name">Editora<br>Verlindt</div>
        <div class="imprint__url">verlindt.example</div>
      </div>
    </div>
  </section>
</main>
</body>
</html>
```